Broschüre in Querformat für Immobilienmakler
Zielgruppe
Immobilienmakler - Überregional tätig - zielgerichtete Vermarktung - Zielgruppe sind Verkäufer oft ältere Menschen
Ich möchte eine Broschüre mit 12 Seiten im Querformat - Die Broschüre sollte der Website harvrenk-immobilien.example ein wenig ähneln.
Aufgabenstellung
klare Linie - schnell erklärbar und übersichtlich - logischer Aufbau - Aufmerksamkeit erwecken durch Bilder - schnelle Info für Querleser - VERTRAUEN - ehrlich und authentisch - nicht Eitel - schnelle Zurechtfindung - Serviceorientiert - Rundumsorglos Paket

```html
<!DOCTYPE html>
<html lang="de">
<head>
<meta charset="utf-8">
<title>Erfolgshonorar: Vergleich</title>
<link rel="stylesheet" href="https://fonts.googleapis.com/css2?family=Poppins:wght@500;600;700;800&display=swap">
<style>
  :root {
    --brand-yellow: #f8b300;
    --ink: #1b1b1b;
    --accent-red: #e3000f;
    --line-navy: #1d3766;
    --page: #ffffff;
    --frame: #6d6d6d;
  }
  * { margin: 0; padding: 0; box-sizing: border-box; }
  html, body { width: 1200px; height: 853px; overflow: hidden; background: var(--page); }
  body { font-family: "Poppins", Arial, sans-serif; color: var(--ink); }
  .page {
    position: relative; width: 1200px; height: 853px;
    border: 2px solid var(--frame); background: var(--page); overflow: hidden;
  }
  .title-band {
    position: absolute; left: 7px; top: 53px; width: 516px; height: 88px;
    background: var(--brand-yellow);
  }
  .title-band h1 {
    position: absolute; left: 86px; top: 6px;
    color: #fff; font-weight: 800; font-size: 35px; line-height: 37px;
  }
  .section-heading {
    position: absolute; left: 811px; top: 207px;
    font-weight: 700; font-size: 28px; letter-spacing: 0.3px;
  }
  .highlight-panel {
    position: absolute; left: 434px; top: 276px; width: 726px; height: 366px;
    background: var(--brand-yellow);
  }
  .cost-column { position: absolute; top: 0; }
  .cost-column h2 {
    position: absolute; top: 313px; width: 100%; text-align: center;
    font-weight: 700; font-size: 18px; white-space: nowrap;
  }
  .cost-row {
    position: absolute; width: 100%; display: flex; justify-content: space-between;
    font-weight: 600; font-size: 13px; line-height: 18px; white-space: nowrap;
  }
  .cost-row .value { font-weight: 700; }
  .cost-row.total { font-size: 14px; }
  .dotted-rule {
    position: absolute; top: 549px; width: 100%; height: 0;
    border-top: 3px dotted var(--ink);
  }
  .column-old { left: 63px; width: 306px; }
  .column-shared { left: 457px; width: 304px; }
  .column-seller { left: 851px; width: 288px; }
  .row-1 { top: 364px; } .row-2 { top: 411px; } .row-3 { top: 460px; }
  .row-4 { top: 509px; } .row-total { top: 580px; }
  .changed { color: var(--accent-red); }
  .approx-sign { position: absolute; left: 786px; top: 573px; width: 40px; height: 32px; }
  .connector { position: absolute; left: 0; top: 0; width: 1200px; height: 853px; pointer-events: none; }
  .difference {
    position: absolute; right: 61px; text-align: right;
    font-weight: 700; font-size: 12.5px; line-height: 16px; white-space: nowrap;
  }
  .difference-1 { top: 689px; }
  .difference-2 { top: 713px; }
</style>
</head>
<body>
<div class="page">
  <div class="title-band"><h1>Erfolgshonorar:<br>vergleich</h1></div>
  <div class="section-heading">VERKÄUFERPROVISI</div>

  <div class="highlight-panel"></div>

  <div class="cost-column column-old">
    <h2>bis 23.12.2020 (alt)</h2>
    <div class="cost-row row-1"><span>Kaufpreis:</span><span class="value">100.000,00 €</span></div>
    <div class="cost-row row-2"><span>Käuferprovision 6 %:</span><span class="value">6.000,00 €</span></div>
    <div class="cost-row row-3"><span>Grunderwerbsteuer 5 %:</span><span class="value">5.000,00 €</span></div>
    <div class="cost-row row-4"><span>Notarkosten 1,5 %</span><span class="value">1.500,00 €</span></div>
    <div class="dotted-rule"></div>
    <div class="cost-row row-total total"><span>Gesamtkosten:</span><span class="value">112.550,00 €</span></div>
  </div>

  <div class="cost-column column-shared">
    <h2>Gesetzliche provisionsteilung</h2>
    <div class="cost-row row-1"><span>Kaufpreis inkl. 3% VK-Prov.</span><span class="value">103.000€</span></div>
    <div class="cost-row row-2"><span>Kauferprovision 3%</span><span class="value">3.090 €</span></div>
    <div class="cost-row row-3"><span>Grunderwerbusteuer 5%</span><span class="value">5.150 €</span></div>
    <div class="cost-row row-4"><span>Notarkosten 1,5%</span><span class="value">1.545€</span></div>
    <div class="dotted-rule"></div>
    <div class="cost-row row-total total"><span>Geesamtkosten</span><span class="value">112.785€</span></div>
  </div>

  <svg class="approx-sign" viewBox="0 0 40 32" aria-hidden="true">
    <path d="M4 13 Q12 3 20 12 T36 11" fill="none" stroke="var(--accent-red)" stroke-width="3" stroke-linecap="round"/>
    <path d="M4 23 Q12 13 20 22 T36 21" fill="none" stroke="var(--accent-red)" stroke-width="3" stroke-linecap="round"/>
  </svg>

  <div class="cost-column column-seller">
    <h2>Verkäuferprovision</h2>
    <div class="cost-row row-1"><span>Kaufpreis</span><span class="value">10<span class="changed">6</span>.000 €</span></div>
    <div class="cost-row row-3"><span>Grunderwerbsteuer 5%</span><span class="value">5.<span class="changed">300</span> €</span></div>
    <div class="cost-row row-4"><span>Notarkosten 1,5%</span><span class="value">1.5<span class="changed">90</span> €</span></div>
    <div class="dotted-rule"></div>
    <div class="cost-row row-total total"><span>Gesamtkosten</span><span class="value">112.<span class="changed">890</span> €</span></div>
  </div>

  <svg class="connector" viewBox="0 0 1200 853" aria-hidden="true">
    <g fill="none" stroke="var(--line-navy)" stroke-width="2">
      <polyline points="564,679 775,679 775,725 985,725"/>
      <polyline points="133,720 445,720 445,778 1065,778 1065,742"/>
    </g>
    <g fill="var(--line-navy)">
      <polygon points="993,725 983,720 983,730"/>
      <polygon points="125,720 135,715 135,725"/>
      <polygon points="1065,734 1060,744 1070,744"/>
    </g>
  </svg>

  <div class="difference difference-1">Differenz 340,00 €</div>
  <div class="difference difference-2">DIfferenz &nbsp;105,00 €</div>
</div>
</body>
</html>
```